Business Card Design for Event Planning Company

Create a business card for event planning company using our new logo. After I pick the design, I will need files made for 6 employees. Our company provides event design & logistics services as well as venue management. The font should be sans serif and complementary to the logo. I will need to know the name of the font selected for the final design. The phone numbers listed should be separated by "." not "-"

Address for the card
PO Box 318, Washington, DC 20019

Card One
Lorna Pettibone
lpettibone@galavoyant.com
202.481.7730

Card Two
Miriam Okonkwo
mokonkwo@galavoyant.com
202.556.2047

Card Three
Tessa Varnholt
tvarnholt@galavoyant.com
978.620.4471

Card Four
Robin Fess
rfess@galavoyant.com
202.718.3362

Card Five
Ada-Rose Pelletan-Uzor
adarose@galavoyant.com
202.839.1205

Card Six
Beatrix Holloway
Beatrix@galavoyant.com
202.492.6618

Target Market(s)

Corporate/Non-Profit

Industry/Entity Type

Event Planning

Contact Information for Business Card

Address for the card

Card One
Lorna Pettibone
lpettibone@galavoyant.com
202.481.7730

Card Two
Miriam Okonkwo
202.556.2047

Card Three
Tessa Varnholt
978.620.4471

Card Four
Robin Fess
rfess@galavoyant.com
202.718.3362

Card Five
Ada-Rose Pelletan-Uzor
202.839.1205

Card Six
Beatrix Holloway
202.492.6618

Font styles to use
Sans Serif

Colors

Designer to choose colors to be used in the design.

Requirements
Must have
• Two-sided with logo
Should not have
• Extra colors or be too busy

```html
<!DOCTYPE html>
<html lang="en">
<head>
<meta charset="utf-8">
<title>Galavoyant Business Card</title>
<link rel="stylesheet" href="https://fonts.googleapis.com/css2?family=Questrial&family=Lato:wght@400&display=swap">
<style>
  :root {
    --stage: #e9e7e4;
    --card-dark: #2a292b;
    --card-dark-tone: #3a393b;
    --card-light: #ffffff;
    --teal: #5ba5a3;
    --ink: #1f1e20;
    --white: #ffffff;
  }
  * { margin: 0; padding: 0; box-sizing: border-box; }
  html, body { width: 900px; height: 1200px; overflow: hidden; }
  body {
    background: var(--stage);
    position: relative;
    font-family: "Questrial", sans-serif;
  }
  .card {
    position: absolute;
    left: 98px;
    width: 714px;
    height: 412px;
    border-radius: 28px;
    overflow: hidden;
    box-shadow: 0 6px 16px rgba(0,0,0,0.25);
  }
  .card-front { top: 145px; background: var(--card-dark); }
  .card-back { top: 633px; background: var(--card-light); }

  .front-texture {
    position: absolute; inset: 0;
    background: radial-gradient(circle at 50% 50%, var(--card-dark-tone) 0%, var(--card-dark) 75%);
  }
  .wordmark {
    position: absolute;
    left: 0; right: 0;
    text-align: center;
    font-family: "Questrial", sans-serif;
    font-size: 60px;
    letter-spacing: 0.5px;
    line-height: 1;
  }
  .card-front .wordmark { top: 210px; color: var(--white); }
  .card-back .wordmark { top: 122px; color: var(--ink); }

  .back-waves { position: absolute; inset: 0; width: 714px; height: 412px; }

  .holder-name {
    position: absolute; top: 200px; left: 0; right: 0;
    text-align: center;
    font-size: 29px;
    color: var(--ink);
    line-height: 1;
  }
  .holder-name .surname { color: var(--teal); }
  .address {
    position: absolute; top: 240px; left: 0; right: 0;
    text-align: center;
    font-family: "Lato", sans-serif;
    font-size: 18px;
    color: var(--ink);
  }
  .contact-row {
    position: absolute; top: 358px; left: 0; right: 0;
    display: flex; justify-content: center; gap: 14px;
    align-items: center;
  }
  .contact-item {
    display: flex; align-items: center; gap: 8px;
    font-family: "Lato", sans-serif;
    font-size: 18px;
    color: var(--white);
  }
  .contact-icon { width: 34px; height: 34px; }
</style>
</head>
<body>

  <section class="card card-front">
    <div class="front-texture" role="img" aria-label="Dark damask floral pattern background"></div>
    <div class="wordmark">galavoyant</div>
  </section>

  <section class="card card-back">
    <svg class="back-waves" viewBox="0 0 714 412" aria-hidden="true">
      <path d="M0 236 C 180 268, 360 318, 714 272 L714 282 C 360 330, 180 284, 0 252 Z" fill="var(--teal)"/>
      <path d="M0 262 C 190 298, 400 328, 714 292 L714 302 C 400 340, 190 314, 0 280 Z" fill="var(--ink)"/>
      <path d="M0 290 C 200 332, 450 344, 714 310 L714 412 L0 412 Z" fill="var(--teal)"/>
    </svg>

    <div class="wordmark">galavoyant</div>
    <div class="holder-name">Lorna <span class="surname">Pettibone</span></div>
    <div class="address">PO Box 318, Washington, DC 20019</div>

    <div class="contact-row">
      <div class="contact-item">
        <svg class="contact-icon" viewBox="0 0 34 34" aria-hidden="true">
          <circle cx="17" cy="17" r="15.5" fill="none" stroke="var(--white)" stroke-width="2"/>
          <path d="M10 14 C10 11, 24 11, 24 14 L22 15.5 L20 14 L14 14 L12 15.5 Z" fill="var(--white)"/>
          <rect x="12" y="16" width="10" height="8" rx="1.5" fill="var(--white)"/>
        </svg>
        <span>202.481.7730</span>
      </div>
      <div class="contact-item">
        <svg class="contact-icon" viewBox="0 0 34 34" aria-hidden="true">
          <circle cx="17" cy="17" r="15.5" fill="none" stroke="var(--white)" stroke-width="2"/>
          <rect x="9" y="11.5" width="16" height="11" rx="1" fill="var(--white)"/>
          <path d="M9.5 12 L17 18 L24.5 12" fill="none" stroke="var(--teal)" stroke-width="1.4"/>
        </svg>
        <span>lpettibone@galavoyant.com</span>
      </div>
    </div>
  </section>

</body>
</html>
```